Book Cover Design for first time business owners

Looking for a design for my book, 'LAYING THE GROUNDWORK' subtitle is
THE REAL ESTATE, DESIGN, & CONSTRUCTION STEPS TO OPENING YOUR RETAIL OR FOOD-SERVICE CONCEPT ON-TIME AND ON BUDGET

If it helps, below is part of the preface:

These pages derive from my experiences and industry standards. This book runs through the budgeting, real estate, design, construction, signage, and equipment processes needed to get any retail or restaurant space open on-time and on budget while saving you time, money, and headaches along the way.

Whether it be a one-off enterprise or franchise, flower shop, or swim center; the steps and procedures are strikingly similar. Whether you’re looking to spend $200,000 or $2,000,000, it’s all largely the same.
This book does not discuss marketing or operations as those items are more concept specific, and outside the confines of this book.
Technically food-service concepts (restaurants, cafés, and bars) are not considered retail. For the basis of this book and to streamline writing, mentions of retail include food-service concepts.

Target Market(s)

First time business Owners looking to construct a retail or food-service concept

Font styles to use
Serif

Requirements
Must have
• I'm open to any designs! Looking for the design to wrap around the front, spine, and back.
• Please include the authors name on the front: Corwin Halbeck. The Authors name size should not be overly intrusive.
• I'm still working on the verbiage for the back of the book. That verbiage will be on the top half of the back.

```html
<!DOCTYPE html>
<html lang="en">
<head>
<meta charset="utf-8">
<title>Laying the Groundwork – Book Cover Wrap</title>
<link rel="stylesheet" href="https://fonts.googleapis.com/css2?family=Playfair+Display:wght@700&family=Playfair+Display+SC:wght@700&display=swap">
<style>
  :root {
    --stage: #3d3d3d;
    --slate: #5c6770;
    --paper: #f9f8f6;
    --title-ink: #545e68;
    --subtitle-ink: #a3a3a3;
    --rule: #b4b4b4;
    --author-ink: #2f2f2f;
    --white: #ffffff;
    --wood-light: #efe3c2;
    --wood-mid: #dcc896;
  }
  * { margin: 0; padding: 0; box-sizing: border-box; }
  html, body { width: 1200px; height: 904px; overflow: hidden; background: var(--stage); }
  .canvas { position: relative; width: 1200px; height: 904px; }
  .wrap { position: absolute; left: 130px; top: 112px; width: 942px; height: 682px; }

  .back-spine { position: absolute; left: 0; top: 0; width: 508px; height: 682px; background: var(--slate); }
  .front { position: absolute; left: 508px; top: 0; width: 434px; height: 682px; background: var(--paper); }

  .back-copy {
    position: absolute; left: 34px; top: 54px; width: 364px;
    font-family: "Playfair Display SC", Georgia, serif; font-weight: 700;
    font-size: 9.4px; line-height: 14px; letter-spacing: 0.9px;
    color: var(--white); text-align: center;
  }
  .author-photo { position: absolute; left: 39px; top: 379px; width: 114px; height: 138px; background: var(--paper); }
  .author-bio {
    position: absolute; left: 168px; top: 408px; width: 240px;
    font-family: "Playfair Display SC", Georgia, serif; font-weight: 700;
    font-size: 7.8px; line-height: 11.6px; letter-spacing: 0.6px;
    color: var(--white); text-align: center;
  }
  .barcode-area { position: absolute; left: 254px; top: 593px; width: 156px; height: 89px; background: var(--paper); }

  .spine-title {
    position: absolute; left: 454px; top: 552px; width: 530px;
    transform-origin: 0 0; transform: rotate(-90deg);
    font-family: "Playfair Display", Georgia, serif; font-weight: 700;
    font-size: 35px; line-height: 40px; letter-spacing: 1px;
    color: var(--white); white-space: nowrap;
  }
  .spine-author {
    position: absolute; left: 472px; top: 662px; width: 120px;
    transform-origin: 0 0; transform: rotate(-90deg);
    font-family: "Playfair Display", Georgia, serif; font-weight: 700;
    font-size: 10px; line-height: 12px; letter-spacing: 4.5px;
    color: var(--white); white-space: nowrap;
  }

  .front-title {
    position: absolute; left: 0; top: 98px; width: 434px;
    font-family: "Playfair Display", Georgia, serif; font-weight: 700;
    font-size: 46px; line-height: 60px; letter-spacing: 1px;
    color: var(--title-ink); text-align: center;
  }
  .title-rule { position: absolute; left: 106px; top: 231px; width: 214px; height: 2px; background: var(--rule); }
  .subtitle {
    position: absolute; left: 54px; top: 243px; width: 326px;
    font-family: "Playfair Display", Georgia, serif; font-weight: 700;
    font-size: 10px; line-height: 14px; letter-spacing: 1.3px;
    color: var(--subtitle-ink); text-align: center; text-transform: uppercase;
  }
  .cover-art { position: absolute; left: 74px; top: 392px; width: 336px; height: 216px; }
  .front-author {
    position: absolute; left: 0; top: 632px; width: 434px;
    font-family: "Playfair Display", Georgia, serif; font-weight: 700;
    font-size: 17px; letter-spacing: 8px;
    color: var(--author-ink); text-align: center;
  }
</style>
</head>
<body>
<div class="canvas">
  <div class="wrap">
    <section class="back-spine">
      <div class="back-copy">
        <p>Lorem ipsum dolor sit amet, consectetuer adipiscing elit, sed diam nonummy nibh euismod tincidunt ut laoreet dolore magna aliquam erat volutpat. Ut wisi enim ad minim veniam, quis nostrud exerci tation ullamcorper suscipit lobortis nisl ut aliquip ex ea commodo consequat. Duis autem vel eum iriure dolor in hendrerit in vulputate velit esse molestie consequat, vel illum dolore eu feugiat nulla facilisis at vero eros et accumsan et iusto odio dignissim qui blandit praesent luptatum zzril delenit augue duis dolore te feugait nulla facilisi.</p>
        <p>Lorem ipsum dolor sit amet, cons ectetuer adipiscing elit, sed diam nonummy nibh euismod tincidunt ut laoreet dolore magna aliquam erat volutpat. Ut wisi enim ad minim veniam, quis nostrud exerci tation ullamcorper suscipit lobortis nisl ut aliquip ex ea</p>
      </div>
      <div class="author-photo"></div>
      <p class="author-bio">Lorem ipsum dolor sit amet, consectetuer adipiscing elit, sed diam nonummy nibh euismod tincidunt ut laoreet dolore magna aliquam erat volutpat. Ut wisi enim ad minim veniam, quis nostrud exerci tation ullamcorper suscipit lobortis nisl ut aliquip ex ea commodo consequat.</p>
      <div class="barcode-area"></div>
      <h2 class="spine-title">LAYING THE GROUNDWORK</h2>
      <p class="spine-author">CORWIN<br>HALBECK</p>
    </section>

    <section class="front">
      <h1 class="front-title">LAYING THE<br>GROUNDWORK</h1>
      <div class="title-rule"></div>
      <p class="subtitle">The Real Estate, Design, &amp; Construction Steps to Opening Your Retail or Food-Service Concept On-Time and On Budget</p>
      <svg class="cover-art" viewBox="0 0 336 216" role="img" aria-label="Wooden jigsaw puzzle pieces, three joined and one apart, on a white surface">
        <defs>
          <radialGradient id="woodGlow" cx="55%" cy="50%" r="55%">
            <stop offset="0%" stop-color="#dcc896"/>
            <stop offset="60%" stop-color="#efe3c2"/>
            <stop offset="100%" stop-color="#f9f8f6"/>
          </radialGradient>
        </defs>
        <rect width="336" height="216" fill="url(#woodGlow)"/>
      </svg>
      <p class="front-author">CORWIN HALBECK</p>
    </section>
  </div>
</div>
</body>
</html>
```